Doctors clinic requires stationary designed

We require various types of stationary to be design based on the logo (attached). We require the following:
- Letterhead (A4 Portrait)
- Business Card (must include UV spot on rear)
- With compliments slip (DL Landscape)
- Appointments card (Folded A6)

We are a young clinical practice which boasts a modern and sophisticated approach to medicine so we require something which feels fresh and modern. Please include colours represented in the logo (contrasting teal and grey). We are calling for creative minds to put forth their ideas and we will be actively providing feedback on all designs.

thank you

Clinic

```html
<!DOCTYPE html>
<html lang="en">
<head>
<meta charset="utf-8">
<title>Dr Clara Whitfield – Business Card</title>
<link href="https://fonts.googleapis.com/css2?family=Open+Sans:wght@400;600;700&display=swap" rel="stylesheet">
<style>
  :root {
    --backdrop: #2a2a2a;
    --teal: #16938d;
    --teal-deep: #0f7f7a;
    --pattern-tone: #128a84;
    --ink: #3a3a3a;
    --ink-soft: #6a6a6a;
    --paper: #f6f6f6;
  }
  * { margin: 0; padding: 0; box-sizing: border-box; }
  html, body {
    width: 1200px; height: 900px; overflow: hidden;
    background: var(--backdrop);
    font-family: "Open Sans", Arial, sans-serif;
  }
  .canvas { position: relative; width: 1200px; height: 900px; }
  .card {
    position: absolute; left: 320px; width: 560px; height: 320px;
    border-radius: 2px;
  }
  .card--front { top: 100px; background: var(--paper); }
  .card--back { top: 480px; background: var(--teal); overflow: hidden; }

  .brand { position: absolute; left: 34px; top: 32px; display: flex; align-items: center; gap: 16px; }
  .brand__mark { width: 62px; height: 62px; border: 3px solid var(--teal); border-radius: 50%; }
  .brand__name { color: var(--teal); font-weight: 700; font-size: 30px; line-height: 1.1; letter-spacing: -0.5px; }
  .brand__role { color: var(--teal); font-weight: 700; font-size: 15px; margin-top: 2px; }

  .contact {
    position: absolute; left: 140px; top: 140px;
    border-left: 3px solid var(--teal); padding-left: 14px;
    color: var(--ink); font-size: 14px; line-height: 1.55;
  }
  .contact__name { font-size: 21px; letter-spacing: 0.5px; line-height: 1.2; }
  .contact__title { font-size: 12px; color: var(--ink-soft); margin-bottom: 4px; }
  .contact__label { color: var(--teal); display: inline-block; width: 50px; }
  .contact__web { color: var(--teal); font-weight: 700; margin-top: 6px; }

  .back-pattern { position: absolute; inset: 0; background: var(--pattern-tone); }
  .back-mark {
    position: absolute; right: 110px; bottom: 80px;
    width: 70px; height: 70px; border: 3px solid #e6efee; border-radius: 50%;
  }
</style>
</head>
<body>
<main class="canvas">
  <section class="card card--front" aria-label="Business card front">
    <div class="brand">
      <div class="brand__mark"></div>
      <div>
        <div class="brand__name">Dr Clara Whitfield</div>
        <div class="brand__role">Obstetrician and Gynaecologist</div>
      </div>
    </div>
    <div class="contact">
      <div class="contact__name">HELENA MARSH</div>
      <div class="contact__title">Manager</div>
      <div><span class="contact__label">Phone</span>917-555-0182</div>
      <div><span class="contact__label">Email</span>helena@clarawhitfield.com</div>
      <div>318 Harbor Ave Suite 140, New York NY</div>
      <div class="contact__web">www.clarawhitfield.com</div>
    </div>
  </section>

  <section class="card card--back" aria-label="Business card back">
    <div class="back-pattern" role="img" aria-label="Tone-on-tone pattern of overlapping circles across the teal back"></div>
    <div class="back-mark"></div>
  </section>
</main>
</body>
</html>
```